Design fur Produktverpackung Haarschmuck
• Geforderte Formate: jpg,ai,eps., pdf
Anforderungen:
Entwerfen Sie ein Brandname für eine Haarschmuck-Linie und ein schönes Design für eine Haarschmuck-Karte (Verpackung). Um die Druckkosten in Schach zu halten, bitte nur ein- oder zweifarbig oder evtl. mit Prägedruck.
Das Design darf peppig daher kommen, soll aber wertig wirken.
Die Stanzrisse finden Sie angehängt (bitte nur auf die Stanzrisse achten, das Design und der Brandname soll neu werden).
Kartenformat: Breite 68mm, Höhe 105mm, mit Euroloch
Unternehmensbeschreibung:
Belieferer von Detailisten
Zielgruppe:
Frauen
Farben, Logo-Favoriten und weitere Anforderungen
Liebe Grüsse
Doris

```html
<!DOCTYPE html>
<html lang="de">
<head>
<meta charset="utf-8">
<title>Lumen Locks – Haarschmuck-Karten</title>
<link rel="stylesheet" href="https://fonts.googleapis.com/css2?family=Great+Vibes&display=swap">
<style>
  :root {
    --backdrop: #565656;
    --card: #c8b397;
    --art-light: #e2d0b0;
    --art-mid: #d6c2a2;
    --cream: #f5e7cb;
    --hole: #2b2420;
  }
  * { margin: 0; padding: 0; box-sizing: border-box; }
  html, body {
    width: 1200px;
    height: 785px;
    overflow: hidden;
    background: var(--backdrop);
  }
  .stage {
    position: relative;
    width: 1200px;
    height: 785px;
  }
  .card {
    position: absolute;
    top: 116px;
    width: 364px;
    height: 580px;
  }
  .card--notched { left: 160px; }
  .card--plain { left: 640px; }
  .card svg {
    position: absolute;
    inset: 0;
    width: 364px;
    height: 580px;
    overflow: visible;
    filter: drop-shadow(0 3px 5px rgba(0, 0, 0, 0.35));
  }
  .card__body { fill: var(--card); }
  .card__hole { fill: var(--hole); }
  .brand {
    position: absolute;
    top: 116px;
    left: 0;
    width: 100%;
    text-align: center;
    font-family: "Great Vibes", cursive;
    font-size: 40px;
    font-weight: 400;
    color: var(--cream);
    line-height: 1;
  }
</style>
</head>
<body>
<main class="stage">

  <section class="card card--notched">
    <svg viewBox="0 0 364 580">
      <defs>
        <clipPath id="notched-shape">
          <path d="M16,0 H348 A16,16 0 0 1 364,16 V170 Q364,178 350,182 V460 Q364,464 364,472 V564 A16,16 0 0 1 348,580 H16 A16,16 0 0 1 0,564 V472 Q0,464 14,460 V182 Q0,178 0,170 V16 A16,16 0 0 1 16,0 Z"/>
        </clipPath>
        <linearGradient id="lock-tone" x1="0" y1="0" x2="1" y2="1">
          <stop offset="0" stop-color="#e2d0b0"/>
          <stop offset="1" stop-color="#d6c2a2"/>
        </linearGradient>
      </defs>
      <path class="card__body" fill-rule="evenodd"
        d="M16,0 H348 A16,16 0 0 1 364,16 V170 Q364,178 350,182 V460 Q364,464 364,472 V564 A16,16 0 0 1 348,580 H16 A16,16 0 0 1 0,564 V472 Q0,464 14,460 V182 Q0,178 0,170 V16 A16,16 0 0 1 16,0 Z
           M150,18 H214 A14,14 0 0 1 214,46 H150 A14,14 0 0 1 150,18 Z"/>
      <g clip-path="url(#notched-shape)">
        <path d="M254,0 H364 V90 C330,60 290,30 254,0 Z" fill="url(#lock-tone)" opacity="0.75"
          role="img" aria-label="Line-art swirl of hair strands in the top corner"/>
        <path d="M0,160 C70,170 130,210 160,270 C180,330 200,380 250,400 C300,415 340,430 364,440 V580 H0 Z"
          fill="url(#lock-tone)" opacity="0.8"
          role="img" aria-label="Flowing line-art illustration of a wavy hair lock with a curled tip"/>
      </g>
      <circle class="card__hole" cx="170" cy="184" r="5"/>
      <circle class="card__hole" cx="166" cy="370" r="5"/>
    </svg>
    <p class="brand">Lumen Locks</p>
  </section>

  <section class="card card--plain">
    <svg viewBox="0 0 364 580">
      <defs>
        <clipPath id="plain-shape">
          <rect x="0" y="0" width="364" height="580" rx="16"/>
        </clipPath>
        <linearGradient id="lock-tone-b" x1="0" y1="0" x2="1" y2="1">
          <stop offset="0" stop-color="#e2d0b0"/>
          <stop offset="1" stop-color="#d6c2a2"/>
        </linearGradient>
      </defs>
      <path class="card__body" fill-rule="evenodd"
        d="M16,0 H348 A16,16 0 0 1 364,16 V564 A16,16 0 0 1 348,580 H16 A16,16 0 0 1 0,564 V16 A16,16 0 0 1 16,0 Z
           M150,18 H214 A14,14 0 0 1 214,46 H150 A14,14 0 0 1 150,18 Z"/>
      <g clip-path="url(#plain-shape)">
        <path d="M254,0 H364 V90 C330,60 290,30 254,0 Z" fill="url(#lock-tone-b)" opacity="0.75"
          role="img" aria-label="Line-art swirl of hair strands in the top corner"/>
        <path d="M0,160 C60,180 100,240 110,300 C120,360 140,400 200,410 C260,420 320,440 364,470 V580 H0 Z"
          fill="url(#lock-tone-b)" opacity="0.8"
          role="img" aria-label="Flowing line-art illustration of a wavy hair lock"/>
      </g>
      <circle class="card__hole" cx="162" cy="184" r="5"/>
      <circle class="card__hole" cx="162" cy="290" r="5"/>
      <circle class="card__hole" cx="162" cy="392" r="5"/>
      <circle class="card__hole" cx="162" cy="488" r="5"/>
    </svg>
    <p class="brand">Lumen Locks</p>
  </section>

</main>
</body>
</html>
```